Meadowline Lawncare by RT

Design a eye catching EDDM postcard for Lawn Care business... 6.5" x 8" EDDM Postcards with required bleed points

There are a few EDDM rules to follow which are.

1. Be sure to add your Postal Indicia it needs to read
“PRST STD ECRWSS U.S. POSTAGE PAID EDDM RETAIL”
in the top right area of your EDDM Flyer Postcard

2. The address area also needs to be filled in with
“****ECRWSS**** Local Postal Customer”

3. Both of these items need to be present on the same side for example both on the back of your EDDM mailer.
Please see the image on the side here for a visual description on how to set up your EDDM mailer correctly. (Attached Sample Template)

Target Market(s)

Home Owners that has a Lawn Care need

Industry/Entity Type

Lawn Care

Font styles to use
Serif

Colors

Designer to choose colors to be used in the design.

Requirements
Must have
• A beautiful background that capture the homeowner eyes when they open their mailbox and see this small card.
• My number: 409-555-0173
• My Name & Email: Dorian Pelham - dopeturfworks@mailcrest.net

```html
<!DOCTYPE html>
<html lang="en">
<head>
<meta charset="utf-8">
<title>Meadowline Lawncare EDDM Postcard</title>
<link rel="stylesheet" href="https://fonts.googleapis.com/css2?family=Raleway:wght@300;400;500;700&family=Montserrat:wght@500;700;800&display=swap">
<style>
  :root {
    --backdrop: #3b2519;
    --white: #ffffff;
    --ink: #141414;
    --accent: #f2c200;
    --dark-1: #4a4a4a;
    --dark-2: #1c1c1c;
    --sky: #5d9ee0;
    --foliage: #3f7a2c;
    --lawn: #5fa532;
    --indicia-line: #333333;
  }
  * { box-sizing: border-box; margin: 0; padding: 0; }
  html, body { width: 1200px; height: 1000px; overflow: hidden; }
  body {
    position: relative;
    background: var(--backdrop);
    font-family: "Raleway", sans-serif;
  }

  /* Front side */
  .postcard-front {
    position: absolute; left: 68px; top: 42px; width: 560px; height: 455px;
    overflow: hidden;
  }
  .front-photo {
    position: absolute; inset: 0;
    background: linear-gradient(180deg, var(--sky) 0%, #a9cdef 12%, var(--foliage) 30%, #2f5f22 52%, var(--lawn) 66%, #4e9228 100%);
  }
  .front-frame {
    position: absolute; left: 28px; top: 44px; width: 504px; height: 389px;
    border: 2px solid var(--white);
  }
  .front-brand {
    position: absolute; left: 162px; top: 26px; width: 210px;
    text-align: center; color: var(--ink);
    font-family: "Montserrat", sans-serif; font-weight: 700; line-height: 1;
  }
  .front-brand .brand-main { display: block; font-size: 24px; letter-spacing: 2px; }
  .front-brand .brand-sub { display: block; font-size: 17px; letter-spacing: 0.5px; margin-top: 3px; }
  .front-email {
    position: absolute; left: 0; right: 0; top: 421px; text-align: center;
  }
  .front-email span {
    display: inline-block; padding: 0 8px; background: #4e9228;
    border-left: 2px solid var(--white); border-right: 2px solid var(--white);
    color: var(--white); font-size: 15px; line-height: 22px;
  }

  /* Back side */
  .postcard-back {
    position: absolute; left: 583px; top: 510px; width: 559px; height: 455px;
    background: var(--white);
  }
  .back-panel {
    position: absolute; left: 0; top: 0; width: 330px; height: 455px;
    background: radial-gradient(ellipse at 65% 35%, var(--dark-1) 0%, #2c2c2c 55%, var(--dark-2) 100%);
  }
  .name-box {
    position: absolute; left: 50px; top: 55px; width: 229px; height: 57px;
    border: 1px solid var(--white); color: var(--white); text-align: center;
  }
  .name-box .first-name {
    display: block; font-size: 16px; font-weight: 400; letter-spacing: 1px;
    margin-top: 10px; line-height: 1;
  }
  .name-box .last-name {
    display: block; font-family: "Montserrat", sans-serif; font-size: 36px;
    font-weight: 800; line-height: 1; margin-top: 3px;
    background: var(--dark-1); padding: 0 4px; width: max-content; margin-left: auto; margin-right: auto;
  }
  .contact-box {
    position: absolute; left: 50px; top: 210px; width: 229px; height: 80px;
    border: 1px solid var(--white); color: var(--white); text-align: center;
  }
  .contact-box .contact-label {
    position: absolute; left: 50%; top: -10px; transform: translateX(-50%);
    background: #333; padding: 0 6px; white-space: nowrap;
    font-size: 17px; font-weight: 500; letter-spacing: 0.5px; line-height: 20px;
  }
  .contact-box .contact-phone {
    display: block; margin-top: 14px; color: var(--accent);
    font-family: "Montserrat", sans-serif; font-weight: 700; font-size: 26px; line-height: 1;
  }
  .contact-box .contact-email {
    display: block; margin-top: 10px; font-size: 13.5px; line-height: 1;
  }
  .back-brand {
    position: absolute; left: 0; width: 330px; top: 362px;
    text-align: center; color: var(--white);
    font-family: "Montserrat", sans-serif; font-weight: 700; line-height: 1;
  }
  .back-brand .brand-main { display: block; font-size: 28px; letter-spacing: 3px; }
  .back-brand .brand-sub { display: block; font-size: 20px; margin-top: 6px; }

  .indicia {
    position: absolute; left: 488px; top: 25px; width: 50px; height: 47px;
    border: 1px solid var(--indicia-line);
    font-family: Arial, sans-serif; font-size: 5.5px; line-height: 7px;
    text-align: center; color: var(--ink); padding-top: 4px;
  }
  .address-block {
    position: absolute; left: 407px; top: 208px; width: 133px; height: 38px;
    border: 1px solid #999; box-shadow: 0 1px 2px rgba(0,0,0,0.25);
    font-family: Arial, sans-serif; font-size: 7.5px; line-height: 9px;
    color: var(--ink); padding: 5px 4px;
  }
</style>
</head>
<body>
  <section class="postcard-front">
    <div class="front-photo" role="img" aria-label="Photo of a freshly striped green lawn beside a house with a patio, shrubs and trees under a blue sky"></div>
    <div class="front-frame"></div>
    <div class="front-brand">
      <span class="brand-main">MEADOWLINE</span>
      <span class="brand-sub">Lawncare</span>
    </div>
    <div class="front-email"><span>dopeturfworks@mailcrest.net</span></div>
  </section>

  <section class="postcard-back">
    <div class="back-panel" role="img" aria-label="Dark monochrome photo of a lawn mower on grass">
      <div class="name-box">
        <span class="first-name">DORIAN</span>
        <span class="last-name">PELHAM</span>
      </div>
      <div class="contact-box">
        <span class="contact-label">CONTACT US AT</span>
        <span class="contact-phone">409.555.0173</span>
        <span class="contact-email">dopeturfworks@mailcrest.net</span>
      </div>
      <div class="back-brand">
        <span class="brand-main">MEADOWLINE</span>
        <span class="brand-sub">Lawncare</span>
      </div>
    </div>
    <div class="indicia">PRST STD<br>ECRWSS<br>U.S. POSTAGE<br>PAID<br>EDDM RETAIL</div>
    <div class="address-block">****************ECRWSS****<br>Local<br>Postal Customer</div>
  </section>
</body>
</html>
```